Business card design for new eCommerce site focusing on integrity and strong businsess tactics

We need a business card that will stand out and be memorable. Something with color that matches our company logo colors. Think high end version of Dealvine. There are 2 logos provided. The parent company is called Bright Harbor Ventures and we are presenting a new and very exciting eCommerce site called KeenTraders.example.

Target Market(s)

Our target markets are in the Activities, Food and Beverage, Health and Beauty

Industry/Entity Type

Marketing

Contact Information for Business Card

We have 4 members that need cards...I will provide all info to the winner of the design contest
Business Address is
48730 West 61st Avenue, Suite C204
Phoenix AZ 85917

Font styles to use
Serif
Sans Serif

Colors

Designer to choose colors to be used in the design.

Requirements
Must have
• The card must be memorable...should be unique in design but must exude integrity and be playful .
• I have provided several colors or our parent company...please feel free to use which ever
Nice to have
• I will leave this up to you. Feel free to use other images of your choosing that wraps around our client.....Activities, Dining, Health, Beauty
Should not have
• just dont be boring

```html
<!DOCTYPE html>
<html lang="en">
<head>
<meta charset="utf-8">
<title>Bright Harbor Ventures – Business Card</title>
<link rel="stylesheet" href="https://fonts.googleapis.com/css2?family=Arimo:wght@700&display=swap">
<style>
  :root {
    --navy: #121f4a;
    --paper: #ffffff;
  }
  html, body {
    margin: 0;
    padding: 0;
    overflow: hidden;
    background: var(--paper);
  }
  .card {
    position: relative;
    width: 1200px;
    height: 686px;
    background: var(--paper);
    overflow: hidden;
    font-family: "Arimo", Arial, sans-serif;
    font-weight: 700;
    color: var(--navy);
  }
  .card__bands {
    position: absolute;
    inset: 0;
  }
  .brand {
    position: absolute;
    left: 40px;
    top: 162px;
    width: 470px;
    text-align: center;
  }
  .brand__mark {
    display: block;
    margin: 0 auto;
  }
  .brand__name {
    margin: 18px 0 0;
    font-size: 50px;
    line-height: 1.05;
    letter-spacing: -0.5px;
  }
  .divider {
    position: absolute;
    left: 642px;
    top: 198px;
    width: 9px;
    height: 299px;
    background: var(--navy);
  }
  .member {
    position: absolute;
    left: 669px;
    top: 220px;
  }
  .member__name {
    margin: 0;
    font-size: 46px;
    line-height: 1;
  }
  .member__address {
    margin: 90px 0 0;
    font-style: normal;
    font-size: 29.5px;
    line-height: 46px;
  }
</style>
</head>
<body>
  <div class="card">
    <svg class="card__bands" width="1200" height="686" viewBox="0 0 1200 686" aria-hidden="true">
      <polygon class="band band--top" points="0,0 1200,0 1200,31 451,31 389,83 0,83" fill="var(--navy)"/>
      <polygon class="band band--bottom" points="0,655 749,655 811,602 1200,602 1200,686 0,686" fill="var(--navy)"/>
    </svg>

    <div class="brand">
      <svg class="brand__mark" width="300" height="300" viewBox="0 0 300 300" aria-hidden="true">
        <circle cx="150" cy="150" r="146" fill="var(--paper)" stroke="var(--navy)" stroke-width="3"/>
        <circle cx="150" cy="150" r="136" fill="var(--navy)"/>
      </svg>
      <p class="brand__name">Bright Harbor<br>Ventures</p>
    </div>

    <div class="divider"></div>

    <div class="member">
      <h1 class="member__name">Member’s Name</h1>
      <address class="member__address">
        48730 West 61st Avenue,<br>
        Suite C204 Phoenix AZ 85917
      </address>
    </div>
  </div>
</body>
</html>
```